Bright Lanterns Business Card

Design of business cards

Target Market(s)

We are aiming as small business owners who need anything from basic business structures, website plans, business processes and quality assurance.

Industry/Entity Type

Business

Colors

Designer to choose colors to be used in the design.

Requirements
Nice to have
• I would prefer one side of the card to use the green from the logo. Prefer to have the same font as the logo.

```html
<!DOCTYPE html>
<html lang="en">
<head>
<meta charset="utf-8">
<title>Bright Lanterns Consulting – Business Card</title>
<link rel="stylesheet" href="https://fonts.googleapis.com/css2?family=Cinzel:wght@400;600&family=Libre+Baskerville:wght@400;700&display=swap">
<style>
  :root {
    --lime: #9ccb2c;
    --lime-soft: #b3d85a;
    --ink: #1e1e1e;
    --paper: #fbfbfb;
    --backdrop: #e6e6e6;
    --shadow: rgba(0, 0, 0, 0.14);
  }
  * { margin: 0; padding: 0; box-sizing: border-box; }
  html, body {
    width: 1200px;
    height: 1200px;
    overflow: hidden;
  }
  body {
    background: radial-gradient(circle at 30% 25%, #f7f7f7 0%, var(--backdrop) 75%);
    position: relative;
    font-family: "Cinzel", serif;
  }
  .card {
    position: absolute;
    left: 250px;
    width: 700px;
    height: 400px;
    border-radius: 4px;
    box-shadow: 0 18px 40px var(--shadow);
    overflow: hidden;
  }
  .card--front { top: 150px; background: var(--lime); }
  .card--back  { top: 650px; background: var(--paper); }

  .wordmark {
    position: absolute;
    display: flex;
    align-items: center;
    gap: 22px;
  }
  .wordmark__dot {
    width: 46px;
    height: 46px;
    border-radius: 50%;
    flex: none;
  }
  .wordmark__name {
    font-family: "Cinzel", serif;
    font-weight: 400;
    font-size: 34px;
    line-height: 1.12;
    letter-spacing: 2px;
  }
  .card--front .wordmark { left: 110px; top: 130px; }
  .card--front .wordmark__dot { background: #ffffff; }
  .card--front .wordmark__name { color: #ffffff; }

  .card--back .wordmark { left: 60px; top: 70px; }
  .card--back .wordmark__dot { background: var(--lime); }
  .card--back .wordmark__name { color: var(--lime); font-size: 30px; }

  .contact-band {
    position: absolute;
    right: 0;
    bottom: 90px;
    width: 330px;
    height: 86px;
    background: var(--lime);
    padding: 14px 22px;
    font-family: "Libre Baskerville", serif;
    color: var(--ink);
  }
  .contact-band__name {
    font-weight: 700;
    font-size: 20px;
    margin-bottom: 8px;
  }
  .contact-band__phone {
    display: flex;
    align-items: center;
    gap: 8px;
    font-size: 14px;
  }
  .contact-band__phone svg { width: 16px; height: 16px; flex: none; }
</style>
</head>
<body>

  <section class="card card--front" aria-label="Card front">
    <div class="wordmark">
      <span class="wordmark__dot"></span>
      <p class="wordmark__name">Bright<br>Lanterns<br>Consulting</p>
    </div>
  </section>

  <section class="card card--back" aria-label="Card back">
    <div class="wordmark">
      <span class="wordmark__dot"></span>
      <p class="wordmark__name">Bright<br>Lanterns<br>Consulting</p>
    </div>
    <div class="contact-band">
      <p class="contact-band__name">Name : xxxx xxx</p>
      <p class="contact-band__phone">
        <svg viewBox="0 0 16 16" aria-hidden="true">
          <circle cx="8" cy="8" r="7.5" fill="#1e1e1e"/>
          <rect x="5.5" y="3.5" width="5" height="9" rx="1" fill="none" stroke="#9ccb2c" stroke-width="1.2"/>
        </svg>
        xxx xxx-xxxx
      </p>
    </div>
  </section>

</body>
</html>
```